Etikett-Design für Olivenöl
Unsere Vorgaben wurden gut aufgenommen. Der erste Entwurf hat uns sofort angesprochen. Wir hatten noch ein paar Modifikationen und das Projekt war sehr schnell erfolgreich abgeschlossen. Wir werden weitere Themen hier beauftragen. Besten Dank.
Zielgruppe
Einzelhandel. Die Zielgruppe ist 30 bis 55 Jahre alt, weiblich sowie männlich.
Aufgabenstellung
Das Label für die 100ml große Flasche soll 13,4 cm x 6,7 cm groß sein.
In der Flasche ist ein hochwertiges natives Olivenöl.
Das Design soll frisch, klar, ansprechend, anziehend und freundlich sein.

```html
<!DOCTYPE html>
<html lang="de">
<head>
<meta charset="utf-8">
<title>Solvera Olivenöl – Etikett</title>
<link href="https://fonts.googleapis.com/css2?family=Bitter:ital,wght@0,300;0,700;1,700;1,800&family=Roboto+Condensed:wght@400;700&display=swap" rel="stylesheet">
<style>
  :root {
    --olive-dark: #566640;
    --olive-lime: #9aab2e;
    --leaf-band: #a9b43a;
    --white: #ffffff;
    --ink: #3c3c3c;
  }
  * { margin: 0; padding: 0; box-sizing: border-box; }
  html, body { width: 1200px; height: 600px; overflow: hidden; background: var(--olive-dark); }
  .label {
    position: relative; width: 1200px; height: 600px;
    background: var(--olive-dark); color: var(--white);
    font-family: "Roboto Condensed", Arial, sans-serif;
  }
  .leaf-band {
    position: absolute; left: 0; top: 0; width: 1200px; height: 98px;
    background: linear-gradient(90deg, #c3cb6a, var(--leaf-band) 50%, #c3cb6a);
  }
  .brand-box {
    position: absolute; left: 499px; top: 0; width: 204px; height: 195px;
    background: var(--white);
    display: flex; align-items: center; justify-content: center; flex-direction: column; gap: 10px;
  }
  .brand-box .dot { width: 14px; height: 14px; border-radius: 50%; background: var(--olive-dark); }
  .brand-name {
    font-family: "Roboto Condensed", Arial, sans-serif; font-weight: 700;
    font-size: 36px; letter-spacing: 1px; color: var(--ink);
  }
  .donation-heart { position: absolute; left: 676px; top: 116px; width: 156px; height: 140px; }
  .slogan {
    position: absolute; left: 38px; top: 122px;
    font-family: "Bitter", Georgia, serif; font-style: italic; font-weight: 800;
    font-size: 44px; line-height: 44px; color: var(--olive-lime);
  }
  .variety { position: absolute; left: 38px; top: 294px; font-size: 20px; }
  .pairing-icons { position: absolute; left: 38px; top: 324px; display: flex; gap: 22px; }
  .pairing-icons svg { width: 32px; height: 30px; stroke: var(--olive-lime); fill: none; stroke-width: 2; stroke-linecap: round; stroke-linejoin: round; }
  .storage { position: absolute; left: 38px; top: 480px; font-size: 20px; line-height: 25.5px; }
  .product-name {
    position: absolute; left: 0; width: 1200px; top: 250px; text-align: center;
    font-family: "Bitter", Georgia, serif; font-style: italic; font-weight: 800;
    font-size: 88px; line-height: 100px; color: var(--white);
  }
  .product-sub {
    position: absolute; left: 0; width: 1200px; top: 348px; text-align: center;
    font-family: "Bitter", Georgia, serif; font-weight: 300; font-size: 24px; color: var(--olive-lime);
  }
  .product-facts {
    position: absolute; left: 0; width: 1200px; top: 427px; text-align: center;
    font-size: 23px; line-height: 29px;
  }
  .volume { position: absolute; left: 0; width: 1200px; top: 534px; text-align: center; font-size: 21px; }
  .bottler { position: absolute; left: 899px; top: 126px; font-size: 20px; line-height: 24.3px; }
  .bottler strong { font-weight: 700; }
  .nutrition { position: absolute; left: 899px; top: 392px; width: 282px; }
  .nutrition h2 { font-size: 17px; font-weight: 700; margin-bottom: 11px; }
  .nutrition table { width: 100%; border-collapse: collapse; font-size: 14px; }
  .nutrition td { padding: 0; height: 19px; }
  .nutrition td.value { text-align: right; padding-right: 10px; }
  .nutrition tr.main td { font-weight: 700; }
  .nutrition tr.main td.value.wide { padding-right: 0; }
</style>
</head>
<body>
<div class="label">
  <div class="leaf-band" role="img" aria-label="Dekoratives Muster aus grünen Olivenblättern"></div>

  <div class="brand-box">
    <span class="dot"></span>
    <span class="brand-name">SOLVERA</span>
  </div>

  <svg class="donation-heart" viewBox="0 0 156 140" aria-label="Wir spenden vom Erlös!">
    <g transform="rotate(14 78 70)">
      <path d="M78 132 C40 104 8 78 12 42 C15 16 48 4 66 24 C72 30 76 36 78 40 C80 36 84 30 90 24 C108 4 141 16 144 42 C148 78 116 104 78 132 Z" fill="var(--olive-lime)"/>
      <g font-family="Bitter, Georgia, serif" font-weight="700" font-size="17" fill="#fff" text-anchor="middle">
        <text x="80" y="50">Wir</text>
        <text x="80" y="68">spenden</text>
        <text x="80" y="86">vom</text>
        <text x="80" y="104">Erlös!</text>
      </g>
    </g>
  </svg>

  <p class="slogan">Kalt,<br>elegant<br>&amp; lecker.</p>

  <p class="variety">Sorte Arbequina, ideal zu:</p>
  <div class="pairing-icons">
    <svg viewBox="0 0 32 30" aria-label="Fisch"><path d="M3 15 C8 7 20 7 25 15 C20 23 8 23 3 15 Z"/><path d="M25 15 L30 10 L30 20 Z"/><circle cx="9" cy="14" r="1"/></svg>
    <svg viewBox="0 0 32 30" aria-label="Brot"><rect x="2" y="10" width="28" height="11" rx="5.5" transform="rotate(-35 16 15)"/><path d="M11 19 L14 15 M15 16 L18 12 M19 13 L22 9"/></svg>
    <svg viewBox="0 0 32 30" aria-label="Gebäck"><path d="M8 15 L10 28 H22 L24 15 Z"/><path d="M6 15 C4 9 10 5 13 7 C14 3 20 3 21 7 C25 5 29 10 26 15 Z"/></svg>
    <svg viewBox="0 0 32 30" aria-label="Salat"><path d="M3 16 H29 C29 24 23 28 16 28 C9 28 3 24 3 16 Z"/><path d="M6 16 C6 8 12 5 16 9 C20 5 26 8 26 16"/></svg>
  </div>

  <p class="storage">Mindestens haltbar bis:<br>siehe Flaschenhals<br>Kühl und dunkel lagern</p>

  <h1 class="product-name">Olivenöl</h1>
  <p class="product-sub">extra nativ · frühe Ernte</p>
  <p class="product-facts">sortenrein &amp; mühlenfrisch<br>kaltgepresst<br>0,17 % Ölsäure</p>
  <p class="volume">100ml</p>

  <address class="bottler" style="font-style:normal">
    <strong>Abgefüllt von Oliveras Mar<br>für Solvera OHG</strong><br>
    Am Lindenhof 12<br>20095 Hamburg<br>Deutschland<br>kontakt@solvera-oel.de
  </address>

  <section class="nutrition">
    <h2>Durchschnittliche Nährwerte pro 100g</h2>
    <table>
      <tr class="main"><td>Energie / Brennwert</td><td class="value wide">3700 kj / 900 kcal</td></tr>
      <tr class="main"><td>Fett</td><td class="value">100 g</td></tr>
      <tr><td>davon gesättigte Fettsäuren</td><td class="value">10,0 g</td></tr>
      <tr class="main"><td>Kohlenhydrate</td><td class="value">0,0 g</td></tr>
      <tr><td>davon Zucker</td><td class="value">0,0 g</td></tr>
      <tr class="main"><td>Eiweiß</td><td class="value">0,0 g</td></tr>
      <tr class="main"><td>Salz</td><td class="value">0,0 g</td></tr>
    </table>
  </section>
</div>
</body>
</html>
```